Ranked amongst the Best Colleges and Programs

the size of the ad is Full Page, with bleed*
8”x 10.75" plus 0.25" bleed'
you have two choices for the tagline .. please chose what ever you think will allow you to make a better ad.
The instructions on the brief are in red
I am looking for a hight quality modern ad to place in local weekly publications that will stand out .
I would like a ad that people will look at and say i would like to see what this ad is all about.
I apprecate creative work.
the ad should not be very crowded and the text should be able to be read.
if you decide to use people in the ad .. (you don't have to ) then it should be a male dressed in white shirt in and sports jacket.. or if you would like you can use a vector and then use male or female people.
please leave one inch on the bottom for the footer

Target Market(s)

potential middle class students from 23-35 years of age

Industry/Entity Type

education

Requirements
Must have
• .the " 98% employment rate" should stand out in the ad.. but should not be the main part of the ad
Nice to have
• creative
Should not have
• Should not be a very busy or crowded ad.. i prefer pictures of men but should be .. in a business suit .. that looks professional- white shirt

```html
<!DOCTYPE html>
<html lang="en">
<head>
<meta charset="UTF-8">
<title>WRU Masters of Accounting Ad</title>
<link rel="stylesheet" href="https://fonts.googleapis.com/css2?family=Barlow:wght@300;400;700;800&display=swap">
<style>
  :root {
    --backdrop: #ececec;
    --paper: #ffffff;
    --ink: #1d1d1d;
    --white: #ffffff;
    --steel-blue: #789cbd;
    --steel-blue-glass: rgba(120, 156, 189, 0.88);
    --photo-light: #dfe3e8;
    --photo-mid: #b9c3cd;
    --photo-dark: #8f9aa6;
  }
  * { margin: 0; padding: 0; box-sizing: border-box; }
  html, body {
    width: 1200px;
    height: 1200px;
    overflow: hidden;
    background: var(--backdrop);
    font-family: "Barlow", Arial, sans-serif;
  }
  .ad-page {
    position: absolute;
    left: 200px;
    top: 66px;
    width: 800px;
    height: 1069px;
    background: var(--paper);
    overflow: hidden;
  }
  .hero-photo {
    position: absolute;
    left: 0;
    top: 0;
    width: 800px;
    height: 694px;
    background:
      radial-gradient(ellipse at 30% 40%, rgba(240, 214, 200, 0.55), transparent 45%),
      radial-gradient(ellipse at 78% 35%, rgba(70, 80, 92, 0.35), transparent 40%),
      linear-gradient(160deg, var(--photo-light) 0%, var(--photo-mid) 55%, var(--photo-dark) 100%);
  }
  .headline {
    position: absolute;
    left: 0;
    width: 800px;
    top: 146px;
    text-align: center;
    color: var(--white);
    text-shadow: 0 2px 6px rgba(0, 0, 0, 0.25);
  }
  .headline-lead {
    font-weight: 400;
    font-size: 36px;
    line-height: 48px;
  }
  .headline-title {
    margin-top: 8px;
    font-weight: 800;
    font-size: 52px;
    line-height: 62px;
    text-transform: uppercase;
  }
  .ranking-box {
    position: absolute;
    left: 56px;
    top: 476px;
    width: 688px;
    height: 303px;
    background: var(--steel-blue-glass);
    color: var(--white);
    text-align: center;
  }
  .ranking-title {
    margin-top: 24px;
    font-weight: 700;
    font-size: 28px;
    line-height: 34px;
    text-transform: uppercase;
  }
  .ranking-list {
    list-style: none;
    font-weight: 400;
    font-size: 23px;
    line-height: 32px;
  }
  .ranking-divider {
    position: absolute;
    left: 48px;
    right: 48px;
    top: 152px;
    height: 2px;
    background: rgba(255, 255, 255, 0.6);
  }
  .stat {
    position: absolute;
    left: 79px;
    top: 160px;
    display: flex;
    align-items: center;
  }
  .stat-figure {
    font-weight: 800;
    font-size: 118px;
    line-height: 130px;
    letter-spacing: -1px;
  }
  .stat-label {
    margin-left: 48px;
    font-weight: 700;
    font-size: 38px;
    line-height: 48px;
    text-transform: uppercase;
    text-align: left;
    letter-spacing: 0.5px;
  }
  .outcome-copy {
    position: absolute;
    left: 67px;
    top: 815px;
    width: 700px;
    font-weight: 400;
    font-size: 21px;
    line-height: 31px;
    color: var(--ink);
  }
</style>
</head>
<body>
  <main class="ad-page">
    <div class="hero-photo" role="img" aria-label="Photo of hands writing with a pen beside a calculator and financial papers"></div>

    <header class="headline">
      <p class="headline-lead">Get ahead faster in your career<br>with a prestigious WRU-</p>
      <h1 class="headline-title">Masters of Accounting<br>Degree</h1>
    </header>

    <section class="ranking-box">
      <h2 class="ranking-title">Ranked Amongst:</h2>
      <ul class="ranking-list">
        <li>Best Colleges-Ledger Review 2023</li>
        <li>Best Masters in Accounting Degree - Academica Global 2023</li>
      </ul>
      <div class="ranking-divider"></div>
      <div class="stat">
        <span class="stat-figure">98%</span>
        <span class="stat-label">Employment<br>Rate</span>
      </div>
    </section>

    <p class="outcome-copy">WRS graduates have gone on to work in various high-quality jobs in top firms, earning impressive six-figure salaries as well as opening successful businesses.</p>
  </main>
</body>
</html>
```